Simple design for eCommerce retailer of Custom Cut Mirror Frames

We need a fresh design for our eCommerce store. Currently, we need a design for each page on the existing site.

Here is the site as it stands right now: glassvela.com

Here is a competitor site that we like. The owner really likes the block look for the home page: framorly.com

Here is a video we would like to feature: https://videohost.example/v/Kp7rTq2LmXa

Here is the color palate, emphasis on the green and purple: https://palettes.example/quiet-bay-theme-48271953/?showPublished=true

Here is an example of a landing page we are currently using: https://glassvela.com/lander-10-off-install/

Font for the site should be the google font Lato

Home page should include the following sections/blocks:

How it works
Shop now
Testimonials
Featured Products
Before and After Gallery
Updates

My team has been slow getting back to me with feedback. I'm pushing them to speed their process up.

Target Market(s)

Women, Ages 35-65+

Number of Pages Required

5+ page

Font styles to use
Sans Serif

Requirements
Must have
• -Before and after gallery
• -Star ratings
• -eCommerce look and feel
• -Info about being able to order free samples
• -Language from the checkmarks on the landing page
• -sleek product page
• -home page should be have a very modern design feel
Should not have
• Product Prices...the user has to use the calculator to determine the price of their purchase.
• Sliders

```html
<!DOCTYPE html>
<html lang="en">
<head>
<meta charset="utf-8">
<title>GlassVela – Updates</title>
<link href="https://fonts.googleapis.com/css2?family=Roboto:wght@300;400;500&display=swap" rel="stylesheet">
<style>
  :root {
    --page: #f6f4f4;
    --ink: #1d1d1d;
    --muted: #8a8a8a;
    --teal: #96c1c2;
    --white: #ffffff;
    --rule: #dedede;
    --spot-blue: #1a8fd6;
    --spot-red: #8a0a36;
    --badge-grey: #6b6b6b;
    --badge-green: #5bb532;
    --link: #555555;
  }
  * { margin: 0; padding: 0; box-sizing: border-box; }
  html, body { width: 1200px; height: 1200px; overflow: hidden; }
  body { background: var(--page); font-family: "Roboto", Arial, sans-serif; color: var(--ink); position: relative; font-weight: 300; }
  .abs { position: absolute; }

  .post-media-top { left: 234px; top: 0; width: 438px; height: 148px;
    background: linear-gradient(90deg, #c9bfb0 0%, #5a5652 35%, #3f3d3b 70%, #6c9a3a 100%); }
  .post-excerpt-top { left: 712px; top: -4px; width: 206px; font-size: 11.2px; line-height: 13.6px; }

  .post-title { left: 234px; top: 210px; font-size: 22.4px; line-height: 27px; font-weight: 400; }
  .post-meta { left: 234px; top: 276px; font-size: 8.8px; color: var(--muted); }
  .post-body { left: 235px; top: 313px; width: 212px; font-size: 11.2px; line-height: 13.5px; }

  .post-media { left: 528px; top: 215px; width: 438px; height: 276px;
    background: radial-gradient(ellipse at 50% 75%, #e8e8e8 0%, #a8a8a8 35%, #2a2a2a 75%, #111 100%); }
  .spot-label { position: absolute; color: var(--white); font-weight: 400; text-align: center; }
  .spot-label.blue { left: 101px; top: 74px; width: 235px; height: 33px; background: var(--spot-blue); font-size: 18.5px; line-height: 33px; }
  .spot-label.red { left: 116px; top: 168px; width: 206px; height: 30px; background: var(--spot-red); font-size: 18px; line-height: 30px; }

  .testimonial-band { left: 0; top: 567px; width: 1200px; height: 258px; background: var(--teal); }
  .testimonial-quote { left: 239px; top: 634px; width: 740px; font-size: 19px; line-height: 23px; font-weight: 400; }
  .testimonial-author { right: 234px; top: 700px; font-size: 11.2px; font-weight: 400; display: flex; align-items: center; gap: 10px; }
  .testimonial-author::before { content: ""; width: 24px; height: 1px; background: var(--ink); }
  .btn-reviews { left: 239px; top: 733px; width: 149px; height: 33px; border: 1px solid var(--ink);
    display: flex; align-items: center; justify-content: center; gap: 12px; font-size: 10px; font-weight: 500; }

  .footer { left: 0; top: 825px; width: 1200px; height: 375px; background: var(--white); }
  .brand { left: 240px; top: 904px; display: flex; align-items: center; gap: 8px; }
  .brand-mark { width: 22px; height: 22px; background: var(--teal); }
  .brand-name { font-size: 22px; font-weight: 400; }
  .social { left: 240px; top: 988px; display: flex; gap: 26px; }
  .social span { width: 12px; height: 12px; border-radius: 50%; background: #555; display: block; }

  .footer-col { top: 887px; }
  .footer-col h4 { font-size: 11px; font-weight: 400; margin-bottom: 20px; text-transform: uppercase; }
  .footer-col li { list-style: none; font-size: 7.2px; color: var(--link); height: 22.4px; font-weight: 400; }
  .col-company { left: 488px; }
  .col-policies { left: 668px; }
  .col-support { left: 858px; }
  .col-support li, .col-policies li { color: #888; }

  .badge { top: 1053px; width: 50px; height: 50px; }
  .badge.grey { left: 846px; border: 1px solid #bbb; background: linear-gradient(#fff 75%, var(--badge-grey) 75%); }
  .badge.green { left: 917px; border: 1px solid var(--badge-green); background: #fff; }
  .footer-rule { left: 0; top: 1080px; width: 820px; height: 1px; background: var(--rule); }

  .copyright { left: 243px; top: 1143px; font-size: 7.4px; color: #888; font-weight: 400; }
  .pay-label { left: 876px; top: 1134px; font-size: 5.6px; color: #999; }
  .pay-row { left: 808px; top: 1144px; display: flex; gap: 3px; align-items: center; }
  .pay-row span { display: block; width: 18px; height: 12px; background: #cfd3da; }
  .pay-row .secure { width: 38px; height: 14px; border-radius: 7px; background: var(--badge-green); margin-left: 4px; }
</style>
</head>
<body>
  <div class="abs post-media-top" role="img" aria-label="Blog header photo of a framed bathroom mirror beside green leaves"></div>
  <p class="abs post-excerpt-top">design trends among home owners and DIYer’s in recent years, and it’s no wonder why! Once you lay your eyes on</p>

  <h2 class="abs post-title">Product Review Spotlight:<br>Lift &amp; Refresh</h2>
  <p class="abs post-meta">January 22nd, 2018 | 0 Comments</p>
  <p class="abs post-body">Bathroom Mirror Frame Kit Review Spot-light: Lift &amp; Refresh There is nothing we love to hear more at GlassVela than words of satisfaction from our custom-ers. So, imagine how we felt when Lift &amp; Refresh</p>
  <div class="abs post-media" role="img" aria-label="Black and white photo of a photo studio with lights and umbrellas">
    <div class="spot-label blue">Product Review Spotlight</div>
    <div class="spot-label red">Bathroom Mirror Frame</div>
  </div>

  <section class="abs testimonial-band"></section>
  <blockquote class="abs testimonial-quote">Great product and great service! Adding frames to our mirrors made all the difference in how the master bath looks. You can’t beat GlassVela for the money!</blockquote>
  <p class="abs testimonial-author">Dana R., Oceanside, Ca</p>
  <a class="abs btn-reviews">SEE ALL REVIEW
    <svg width="18" height="12" viewBox="0 0 18 12"><path d="M0 6h16M11 1l5 5-5 5" fill="none" stroke="#1d1d1d" stroke-width="1.3"/></svg>
  </a>

  <footer class="abs footer"></footer>
  <div class="abs brand"><span class="brand-mark"></span><span class="brand-name">GlassVela</span></div>
  <div class="abs social"><span></span><span></span><span></span><span></span><span></span></div>

  <div class="abs footer-col col-company"><h4>Company Info</h4>
    <ul><li>glassvela.com</li><li>About Us</li><li>Privacy Policy</li><li>Terms and Conditions</li><li>Security On Our Site</li></ul></div>
  <div class="abs footer-col col-policies"><h4>Policies &amp; Product Info</h4>
    <ul><li>Our Guarantee</li><li>Shipping</li><li>Product Care</li><li>Return Policy</li></ul></div>
  <div class="abs footer-col col-support"><h4>Services &amp; Support</h4>
    <ul><li>FAQ</li><li>Customer Support</li><li>Contact Us</li></ul></div>

  <div class="abs badge grey"></div>
  <div class="abs badge green"></div>
  <div class="abs footer-rule"></div>

  <p class="abs copyright">© Copyright 2019 &nbsp;|&nbsp; glassvela.com &nbsp;|&nbsp; All Rights Reserved &nbsp;|&nbsp; Website by Harbor Pixel Studio &amp; Loom Web Works</p>
  <p class="abs pay-label">Payment Options</p>
  <div class="abs pay-row"><span></span><span></span><span></span><span></span><span></span><span></span><span class="secure"></span></div>
</body>
</html>
```